Tarwin Project Consulting

I need a logo and business card design for a small business operating in the management consulting and contractor space, predominantly in local and state government. I specialise in project management, financial consulting, people and culture, procurement, ICT transformation and contracting for corporate support areas of organisations.

Industry/Entity Type

Business

```html
<!DOCTYPE html>
<html lang="en">
<head>
<meta charset="utf-8">
<title>Tarwin Project Consulting – Business Cards</title>
<link href="https://fonts.googleapis.com/css2?family=Roboto:ital,wght@0,400;0,700;1,400&family=Roboto+Condensed:wght@700&display=swap" rel="stylesheet">
<style>
  :root {
    --stage: #1b1b1d;
    --brand-blue: #1c72bd;
    --brand-blue-light: #3f8fd0;
    --ink: #1e1e1e;
    --ink-grey: #4a4a4a;
    --paper: #ffffff;
  }
  * { box-sizing: border-box; margin: 0; padding: 0; }
  html, body { width: 1200px; height: 964px; overflow: hidden; }
  body {
    background: var(--stage);
    position: relative;
    font-family: "Roboto", Arial, sans-serif;
  }
  .card {
    position: absolute;
    border-radius: 22px;
    overflow: hidden;
    box-shadow: 0 14px 30px rgba(0,0,0,.55);
  }
  /* Back of card */
  .card-back {
    left: 590px; top: 80px;
    width: 540px; height: 310px;
    background: linear-gradient(120deg, var(--brand-blue) 0%, var(--brand-blue-light) 50%, var(--brand-blue) 100%);
    color: var(--paper);
    display: flex; flex-direction: column; align-items: center; justify-content: center;
  }
  .wordmark { text-align: center; }
  .wordmark-name {
    font-family: "Roboto Condensed", Arial, sans-serif;
    font-weight: 700;
    font-size: 72px;
    line-height: 1;
    letter-spacing: 1px;
  }
  .wordmark-tagline {
    font-family: "Roboto Condensed", Arial, sans-serif;
    font-weight: 700;
    font-size: 17px;
    letter-spacing: 4px;
    margin-top: 6px;
  }
  .card-back .website { margin-top: 26px; font-size: 16px; }

  /* Front of card */
  .card-front {
    left: 70px; top: 470px;
    width: 640px; height: 366px;
    background: var(--paper);
  }
  .card-front .band {
    position: absolute; left: 0; right: 0; bottom: 0; height: 40px;
    background: linear-gradient(90deg, var(--brand-blue) 0%, var(--brand-blue-light) 45%, var(--brand-blue) 100%);
  }
  .card-front .wordmark {
    position: absolute; left: 40px; top: 100px; width: 250px;
  }
  .card-front .wordmark-name { color: var(--brand-blue); font-size: 70px; }
  .card-front .wordmark-tagline { color: var(--ink-grey); font-size: 16px; }
  .divider {
    position: absolute; left: 316px; top: 70px; width: 2px; height: 200px;
    background: var(--brand-blue);
  }
  .contact { position: absolute; left: 340px; top: 72px; color: var(--ink); }
  .person-name { color: var(--brand-blue); font-weight: 700; font-size: 24px; }
  .person-role { font-weight: 700; font-size: 15px; margin-bottom: 12px; }
  .address { font-size: 16px; line-height: 1.35; margin-bottom: 12px; }
  .contact-line { display: flex; align-items: center; gap: 10px; font-size: 16px; line-height: 1.5; }
  .contact-line svg { width: 15px; height: 15px; flex: none; }
  .contact-line .highlight { color: var(--brand-blue); }
</style>
</head>
<body>

  <section class="card card-back" aria-label="Business card back">
    <div class="wordmark">
      <div class="wordmark-name">Tarwin</div>
      <div class="wordmark-tagline">PROJECT CONSULTING</div>
    </div>
    <p class="website">www.tarwinconsulting.com</p>
  </section>

  <section class="card card-front" aria-label="Business card front">
    <div class="wordmark">
      <div class="wordmark-name">Tarwin</div>
      <div class="wordmark-tagline">PROJECT CONSULTING</div>
    </div>
    <div class="divider"></div>
    <div class="contact">
      <p class="person-name">Liam Hartley</p>
      <p class="person-role">Director</p>
      <p class="address">14 Banksia Street<br>Mosman NSW 2088</p>
      <p class="contact-line">
        <svg viewBox="0 0 16 16" fill="none" stroke="#1c72bd" stroke-width="1.4"><rect x="4" y="1" width="8" height="14" rx="1.5"/><line x1="7" y1="12.5" x2="9" y2="12.5"/></svg>
        (123) 555 0148
      </p>
      <p class="contact-line">
        <svg viewBox="0 0 16 16" fill="#1c72bd"><path d="M1 3h14v10H1z"/><path d="M1 3l7 6 7-6" fill="none" stroke="#fff" stroke-width="1.2"/></svg>
        info@tarwinconsulting.com
      </p>
      <p class="contact-line">
        <svg viewBox="0 0 16 16" fill="none" stroke="#1c72bd" stroke-width="1.3"><circle cx="8" cy="8" r="6.5"/><ellipse cx="8" cy="8" rx="3" ry="6.5"/><line x1="1.5" y1="8" x2="14.5" y2="8"/></svg>
        <span>www.<span class="highlight">tarwinconsulting</span>.com</span>
      </p>
    </div>
    <div class="band"></div>
  </section>

</body>
</html>
```